Investment Company Business Card Design

We need a Business Card design for a new company based in Boston called "Velm Investment". We are cooperating with local real estate and construction companies. Our company is very actively and aggressively acquiring primarily residential investment properties either to buy and hold long term or for purposes or renovating and repositioning for re-sale in the market. In addition, we undertake some development projects and acquisitions as opportunities present themselves. the final design should contains information about “Velm" the river boat. we are tenacious, indomitable, and the business have a favorable wind throughout the voyage for all our investment.
sample Info. on Design:
Tusa Merrick
CEO
555-xxx-xxxx
418 Harlow St. Suite 507, Boston, MA 02111
Please provide a template also, that we can edit the info later.
Reason: i just got new LOGO Design attached will be use in Business Card Design.
Construction

```html
<!DOCTYPE html>
<html lang="en">
<head>
<meta charset="utf-8">
<title>Velm Investment — Business Card</title>
<link rel="stylesheet" href="https://fonts.googleapis.com/css2?family=Exo+2:wght@400;500;600&display=swap">
<style>
  :root {
    --bg: #9c9c9c;
    --card-white: #f7f7f7;
    --card-black: #1c1c1c;
    --gold-dark: #c79a43;
    --gold-light: #f1cd7d;
    --band-grey: #8a8a8a;
    --silver: #d9d9d9;
    --ink: #2b2b2b;
    --ink-soft: #555555;
  }
  * { box-sizing: border-box; margin: 0; padding: 0; }
  html, body { width: 1200px; height: 895px; overflow: hidden; }
  body {
    background: var(--bg);
    font-family: "Exo 2", sans-serif;
    position: relative;
  }
  .card {
    position: absolute;
    top: 292px;
    width: 540px;
    height: 310px;
    overflow: hidden;
    box-shadow: 0 10px 26px rgba(0,0,0,0.28);
  }
  .card--front { left: 45px; background: var(--card-white); }
  .card--back { left: 615px; background: var(--card-black); }

  /* front */
  .brand {
    position: absolute;
    left: 24px;
    top: 30px;
    display: flex;
    align-items: center;
    gap: 10px;
    color: var(--gold-dark);
    font-weight: 600;
    font-size: 26px;
    letter-spacing: 1px;
    text-transform: uppercase;
  }
  .brand__dot {
    width: 14px; height: 14px; border-radius: 50%;
    background: var(--gold-dark);
  }
  .holder {
    position: absolute;
    right: 26px;
    top: 76px;
    text-align: right;
  }
  .holder__name {
    font-size: 19px; font-weight: 500; letter-spacing: 1.5px;
    color: var(--ink); text-transform: uppercase;
  }
  .holder__role {
    font-size: 9px; letter-spacing: 1px; color: var(--ink-soft);
    text-transform: uppercase; margin-top: 3px;
  }
  .contact-band { position: absolute; left: 0; top: 122px; }
  .contact {
    position: absolute;
    top: 170px;
    font-size: 12px;
    line-height: 17px;
    color: var(--ink);
    letter-spacing: 0.3px;
  }
  .contact--web { left: 22px; }
  .contact--address { left: 198px; }
  .contact--phone { left: 388px; }
  .gold-band {
    position: absolute; left: 0; right: 0; bottom: 0; height: 62px;
    background: linear-gradient(90deg, var(--gold-dark), var(--gold-light) 45%, var(--gold-dark));
  }
  .gold-band::before {
    content: ""; position: absolute; left: 0; right: 0; top: -7px; height: 7px;
    background: var(--silver);
  }

  /* back */
  .back-band {
    position: absolute; left: 0; right: 0; height: 50px;
    background: linear-gradient(90deg, var(--gold-dark), var(--gold-light) 50%, var(--gold-dark));
  }
  .back-band--top { top: 0; }
  .back-band--bottom { bottom: 0; }
  .back-notches { position: absolute; left: 0; top: 0; }
  .back-brand {
    position: absolute; left: 0; right: 0; top: 137px;
    display: flex; justify-content: center; align-items: center; gap: 12px;
    color: var(--gold-light);
    font-weight: 600; font-size: 30px; letter-spacing: 1.5px;
    text-transform: uppercase;
  }
  .back-brand .brand__dot { background: var(--gold-light); width: 16px; height: 16px; }
</style>
</head>
<body>

<section class="card card--front" aria-label="Business card front">
  <div class="brand"><span class="brand__dot"></span>Velm Investment</div>

  <div class="holder">
    <p class="holder__name">Tusa Merrick</p>
    <p class="holder__role">CEO</p>
  </div>

  <svg class="contact-band" width="540" height="36" viewBox="0 0 540 36" aria-hidden="true">
    <polygon points="0,0 168,0 184,18 168,36 0,36" fill="var(--band-grey)"/>
    <polygon points="178,0 356,0 372,18 356,36 178,36 194,18" fill="var(--band-grey)"/>
    <polygon points="366,0 540,0 540,36 366,36 382,18" fill="var(--band-grey)"/>
    <!-- globe -->
    <g fill="none" stroke="#fff" stroke-width="1.6" transform="translate(34,18)">
      <circle r="10"/>
      <ellipse rx="4.5" ry="10"/>
      <line x1="-10" y1="0" x2="10" y2="0"/>
      <line x1="-8.5" y1="-5" x2="8.5" y2="-5"/>
      <line x1="-8.5" y1="5" x2="8.5" y2="5"/>
    </g>
    <!-- pin -->
    <g transform="translate(232,18)">
      <path d="M0,11 C-6,3 -7,0 -7,-3 A7,7 0 0 1 7,-3 C7,0 6,3 0,11 Z" fill="#fff"/>
      <circle cx="0" cy="-3" r="2.6" fill="var(--band-grey)"/>
    </g>
    <!-- phone -->
    <g transform="translate(420,18)" fill="none" stroke="#fff" stroke-width="1.6">
      <rect x="-6" y="-11" width="12" height="22" rx="2"/>
      <line x1="-3" y1="7" x2="3" y2="7"/>
    </g>
  </svg>

  <p class="contact contact--web">hello@velminvest.com<br>www.velminvest.com</p>
  <p class="contact contact--address">418 Harlow St. Suite 507<br>Boston, MA 02111</p>
  <p class="contact contact--phone">555-xxx-xxxx<br>555-xxx-xxxx</p>

  <div class="gold-band"></div>
</section>

<section class="card card--back" aria-label="Business card back">
  <div class="back-band back-band--top"></div>
  <div class="back-band back-band--bottom"></div>
  <svg class="back-notches" width="540" height="310" viewBox="0 0 540 310" aria-hidden="true">
    <polygon points="150,50 170,50 186,34 166,34" fill="var(--silver)"/>
    <polygon points="150,50 166,34 160,34 144,50" fill="#111"/>
    <polygon points="380,50 400,50 416,34 396,34" fill="var(--silver)"/>
    <polygon points="150,260 170,260 186,276 166,276" fill="var(--silver)"/>
    <polygon points="380,260 400,260 416,276 396,276" fill="var(--silver)"/>
    <polygon points="374,260 380,260 396,276 390,276" fill="#111"/>
  </svg>
  <div class="back-brand"><span class="brand__dot"></span>Velm Investment</div>
</section>

</body>
</html>
```